Label Design for Saffron Company

We need a label design that is unique for our container. The item inside the container is Saffron, and it is 5g in weigh. We need on the label our logo, the weight and quality. Here is the exactly what we want. We want the background to be black for the label and the design to present royalty, and premium quality.

Premium Quality
Grade A+ Premium Saffron
100% Natural and Pure
www.VelmoraSpice.com

Target Market(s)

Everyone

Requirements
Must have
• Black background, golden border design. Unique design, that show premium and royalty.
Nice to have
• The logo is attached with transparent background so you can show exactly how things look like.
Should not have
• different colors that are not part of the logo.

```html
<!DOCTYPE html>
<html lang="en">
<head>
<meta charset="utf-8">
<title>Velmora Spice – Saffron Tin Label</title>
<link rel="stylesheet" href="https://fonts.googleapis.com/css2?family=Cinzel:wght@400;500&display=swap">
<style>
  :root {
    --backdrop: #3b3b3b;
    --label-light: #585858;
    --label-dark: #2c2c2c;
    --rim: #1a1a1a;
    --gold: #d9c58f;
    --gold-deep: #b89e5e;
    --ivory: #f4f1ea;
  }
  html, body {
    margin: 0;
    padding: 0;
    width: 1200px;
    height: 857px;
    overflow: hidden;
    background: var(--backdrop);
  }
  .label {
    display: block;
    width: 1200px;
    height: 857px;
  }
  .label text {
    font-family: "Cinzel", "Times New Roman", serif;
  }
  .ring-fine { fill: none; stroke: var(--gold); stroke-width: 1.4; }
  .ring-dots { fill: none; stroke: var(--gold); stroke-width: 3; stroke-linecap: round; stroke-dasharray: 0 6.5; }
  .arc-caption { fill: var(--ivory); font-size: 15px; letter-spacing: 3px; }
  .brand-mark { fill: none; stroke: var(--gold-deep); stroke-width: 2; }
  .brand-name { fill: var(--ivory); font-weight: 400; }
  .brand-name--top { font-size: 40px; letter-spacing: 10px; }
  .brand-name--bottom { font-size: 64px; letter-spacing: 4px; }
  .web-address { fill: var(--gold); font-size: 20px; letter-spacing: 1.5px; }
  .net-weight { fill: var(--gold); font-size: 18px; letter-spacing: 1px; }
</style>
</head>
<body>
<svg class="label" viewBox="0 0 1200 857" xmlns="http://www.w3.org/2000/svg" aria-label="Velmora Spice saffron tin label">
  <defs>
    <radialGradient id="label-face" cx="50%" cy="55%" r="55%">
      <stop offset="0%" stop-color="var(--label-light)"/>
      <stop offset="100%" stop-color="var(--label-dark)"/>
    </radialGradient>
    <path id="caption-top" d="M 300,428 A 300 300 0 0 1 900,428"/>
    <path id="caption-bottom" d="M 288,428 A 312 312 0 0 0 912,428"/>
  </defs>

  <!-- tin lid -->
  <circle class="lid-rim" cx="600" cy="428" r="405" fill="var(--rim)"/>
  <circle class="label-face" cx="600" cy="428" r="375" fill="url(#label-face)"/>

  <!-- golden border -->
  <circle class="ring-fine" cx="600" cy="428" r="350"/>
  <circle class="ring-dots" cx="600" cy="428" r="340"/>
  <circle class="ring-fine" cx="600" cy="428" r="329"/>
  <path class="ring-fine" d="M 763.6,194.6 A 285 285 0 0 1 742.5,674.8"/>
  <path class="ring-fine" d="M 457.5,674.8 A 285 285 0 0 1 436.4,194.6"/>

  <!-- curved captions -->
  <text class="arc-caption"><textPath href="#caption-top" startOffset="50%" text-anchor="middle">GRADE A+ PREMIUM SAFFRON</textPath></text>
  <text class="arc-caption"><textPath href="#caption-bottom" startOffset="50%" text-anchor="middle">100% NATURAL AND PURE</textPath></text>

  <!-- brand -->
  <rect class="brand-mark" x="555" y="250" width="90" height="90" rx="14"/>
  <text class="brand-name brand-name--top" x="600" y="420" text-anchor="middle">VELMORA</text>
  <text class="brand-name brand-name--bottom" x="600" y="492" text-anchor="middle">SPICE</text>
  <text class="web-address" x="600" y="540" text-anchor="middle">WWW.VELMORASPICE.COM</text>

  <text class="net-weight" x="600" y="615" text-anchor="middle">5G</text>
</svg>
</body>
</html>
```